VeloRoot Sample Packaging Design

We need a design - with assistance on logo and colours - of a box containing sample sachets of a new natural sports supplement for endurance athletes.
We have an idea of logo and colours but would like input, ideas and assistance to create a cool new brand.

The product is based on natural beetroot powder which is scientifically backed to improve sports performance.
We like clean minimal branding that looks scientific - such as Kestrel Fuel, Stack Grains, Cortex Well Max and TuL Omni Drive sachets.

Attached is the type of package we will be using with matt black sachets, so clean white with potentially a beetroot colour (hex 691a40??) and grey (a3b2c2??) but we would like your professional and creative input.

I have attached a rough logo mock up of the logo I designed, happy for you to develop this by making it a bit cleaner (left edges angled or curved maybe- change font also maybe??) or your own ideas if clean, simple and effective. I based mine off the Far Meridian logo and PB works well with VeloRoot and Personal Best.

The final design should be clean, minimalist, high end sports supplement with a science and natural beetroot feel.
Box size: 300mm x 130mm x 14mm

Target Market(s)

Elite athletes and professionals wanting natural and science-backed supplements that work. Probably mainly men.
The customers are long distance sportspeople and NOT bodybuilders! Including triathletes, cyclists, long distance runners and swimmers.
The brand must also appeal to club level athletes and weekend warriors (but this should be easy if it's targeted at elite level first)

Industry/Entity Type

Supplement

Font styles to use
Sans Serif

Colors

Designer to choose colors to be used in the design.

Requirements
Must have
• - New logo (I like the Far Meridian logo but open to new ideas!)
• - Clean, scientific look with a twist of "I'm natural and not full of sports supplement junk!!"
• - A shade of beetroot red/purple as the signature colour, without looking too feminine.
• - Our slogan is "Beat your best"
Should not have
• A bodybuilder look.

```html
<!DOCTYPE html>
<html lang="en">
<head>
<meta charset="utf-8">
<title>VeloRoot Sample Box</title>
<link rel="stylesheet" href="https://fonts.googleapis.com/css2?family=Questrial&family=Michroma&family=Oswald:wght@200&display=swap">
<style>
  :root {
    --backdrop: #4a1030;
    --beetroot: #691a40;
    --graphite: #3a3a3c;
    --side-black: #000000;
    --side-text: #b9b9b9;
    --face-light: #f4f6f8;
    --face-mid: #dfe3e8;
    --face-grey: #c9ced5;
  }
  * { margin: 0; padding: 0; box-sizing: border-box; }
  html, body {
    width: 1200px; height: 1200px; overflow: hidden;
    background: var(--backdrop);
  }
  .box-net {
    position: absolute; left: 98px; top: 380px;
    width: 1003px; height: 440px;
  }
  .side-panel {
    position: absolute; top: 0; width: 43px; height: 396px;
    background: var(--side-black);
    display: flex; align-items: center; justify-content: center;
  }
  .side-panel--left { left: 0; }
  .side-panel--right { right: 0; }
  .side-slogan {
    font-family: "Oswald", sans-serif; font-weight: 200;
    font-size: 15px; letter-spacing: 1px; color: var(--side-text);
    writing-mode: vertical-rl; white-space: nowrap;
  }
  .side-panel--right .side-slogan { transform: rotate(180deg); }
  .front-face {
    position: absolute; left: 43px; top: 0; width: 916px; height: 396px;
    overflow: hidden;
    background:
      radial-gradient(ellipse 700px 300px at 75% 0%, rgba(255,255,255,0.55), rgba(255,255,255,0) 70%),
      linear-gradient(160deg, var(--face-mid) 0%, var(--face-light) 45%, var(--face-mid) 75%, var(--face-light) 100%);
  }
  .texture-field {
    position: absolute; top: 0; height: 100%; width: 300px;
    opacity: 0.6;
  }
  .texture-field--left {
    left: 0;
    background: linear-gradient(90deg, var(--face-grey), rgba(201,206,213,0));
  }
  .texture-field--right {
    right: 0;
    background: linear-gradient(270deg, var(--face-grey), rgba(201,206,213,0));
  }
  .hero-name {
    position: absolute; left: 40px; top: 140px;
    font-family: "Questrial", sans-serif; font-size: 92px;
    color: var(--beetroot); line-height: 1; letter-spacing: -2px;
  }
  .brand-lockup {
    position: absolute; left: 478px; top: 170px;
    display: flex; align-items: center; gap: 16px;
  }
  .brand-mark {
    width: 22px; height: 22px; background: var(--beetroot);
  }
  .brand-name {
    font-family: "Questrial", sans-serif; font-size: 60px;
    color: var(--beetroot); line-height: 1; letter-spacing: -1px;
  }
  .tagline {
    position: absolute; left: 483px; top: 309px; width: 382px; height: 43px;
    border-top: 1px solid var(--graphite); border-bottom: 1px solid var(--graphite);
    display: flex; align-items: center; justify-content: center;
    font-family: "Michroma", sans-serif; font-size: 20px; letter-spacing: 5px;
    color: var(--graphite); white-space: nowrap;
  }
  .tuck-flap {
    position: absolute; left: 44px; top: 396px; width: 914px; height: 44px;
    background: var(--beetroot);
  }
</style>
</head>
<body>
  <div class="box-net">
    <div class="side-panel side-panel--left"><span class="side-slogan">BEAT YOUR BEST</span></div>
    <div class="front-face">
      <div class="texture-field texture-field--left" role="img" aria-label="Soft grey diamond texture"></div>
      <div class="texture-field texture-field--right" role="img" aria-label="Soft grey diamond texture"></div>
      <div class="hero-name">VeloRoot</div>
      <div class="brand-lockup">
        <span class="brand-mark"></span>
        <span class="brand-name">VeloRoot</span>
      </div>
      <div class="tagline">BEAT YOUR BEST</div>
    </div>
    <div class="side-panel side-panel--right"><span class="side-slogan">BEAT YOUR BEST</span></div>
    <div class="tuck-flap"></div>
  </div>
</body>
</html>
```